Modern and Improved business card design for Family Dental Practice

We have 2 sets of logo we have designed and now just need a business card layout and design for the office. Colors are on the logo. We can choose which logo we want to go with . The font can be changed to whatever seems modern and relevant. We are family dental office that has been open for over 15 years in South Austin Texas.

Target Market(s)

Handout Business cards to referrals and specialists

Industry/Entity Type

Dental

Contact Information for Business Card

We need address, phone, website and email address. 4830 North Maple Loop Suite 208 , Austin,Texas 78392....phone: 512-847-3195.....email- info@bluepinedental.example....website - BluePineDental.example

Font styles to use
Serif
Decorative

Requirements
Must have
• my logo. We have 2 logos, but we can use just one or if we can incorporate one on one side and the other on the other side.
Nice to have
• Really just need a modern look and clean that incorporates the logo and colors .

```html
<!DOCTYPE html>
<html lang="en">
<head>
<meta charset="utf-8">
<title>Blue Pine Family Dentistry – Business Card</title>
<link rel="stylesheet" href="https://fonts.googleapis.com/css2?family=Didact+Gothic&family=Arimo:wght@400;700&display=swap">
<style>
  :root {
    --stage: #e9e7e3;
    --card-white: #fbfbfa;
    --card-black: #1b1b1c;
    --ink: #1a1a1a;
    --ink-soft: #4a4a4a;
    --green: #1f7d1a;
    --green-deep: #146a12;
    --green-light: #9bb04a;
    --edge: #2a8a1f;
  }
  * { margin: 0; padding: 0; box-sizing: border-box; }
  html, body { width: 1200px; height: 768px; overflow: hidden; }
  body {
    background: var(--stage);
    display: flex;
    flex-direction: column;
    align-items: center;
    justify-content: center;
    gap: 40px;
    font-family: "Arimo", Arial, sans-serif;
  }
  .card {
    width: 560px;
    height: 320px;
    position: relative;
    border-bottom: 3px solid var(--edge);
    box-shadow: 0 6px 18px rgba(0,0,0,0.18);
  }

  /* Back side */
  .card--back {
    background: var(--card-black);
    display: flex;
    align-items: center;
    justify-content: center;
    gap: 26px;
  }
  .brand-dot {
    width: 96px; height: 96px;
    border-radius: 50%;
    background: var(--green);
  }
  .card--back .brand-name {
    font-family: "Didact Gothic", sans-serif;
    color: #ffffff;
    font-size: 44px;
    line-height: 0.95;
    letter-spacing: 1px;
  }
  .card--back .practice-type {
    font-family: "Didact Gothic", sans-serif;
    color: var(--green);
    font-size: 15px;
    letter-spacing: 2px;
    margin-top: 8px;
  }

  /* Front side */
  .card--front { background: var(--card-white); }
  .front-info {
    position: absolute;
    left: 40px; top: 30px;
  }
  .front-info .brand-name {
    font-family: "Didact Gothic", sans-serif;
    color: var(--ink);
    font-size: 40px;
    line-height: 0.95;
    letter-spacing: 1px;
  }
  .front-info .practice-type {
    font-family: "Didact Gothic", sans-serif;
    color: var(--green);
    font-size: 15px;
    letter-spacing: 2px;
    margin-top: 8px;
  }
  .person-name {
    color: var(--green-deep);
    font-weight: 700;
    font-size: 18px;
    margin-top: 14px;
  }
  .person-title {
    color: var(--ink-soft);
    font-size: 12px;
    margin-top: 1px;
  }
  .address {
    color: var(--ink);
    font-size: 13px;
    line-height: 1.3;
    margin-top: 10px;
  }
  .contact-list { list-style: none; margin-top: 6px; }
  .contact-list li {
    display: flex;
    align-items: center;
    gap: 8px;
    color: var(--ink);
    font-size: 13px;
    line-height: 1.45;
  }
  .contact-list svg { width: 11px; height: 11px; fill: var(--ink); flex: none; }

  .front-mark {
    position: absolute;
    right: 48px; top: 70px;
    display: flex;
    flex-direction: column;
    align-items: center;
    gap: 12px;
  }
  .front-mark .brand-dot { width: 150px; height: 150px; }
  .front-mark .brand-name {
    font-family: "Didact Gothic", sans-serif;
    color: var(--green);
    font-size: 18px;
    letter-spacing: 2px;
  }
</style>
</head>
<body>

  <section class="card card--back" aria-label="Card back">
    <div class="brand-dot"></div>
    <div class="brand-lockup">
      <div class="brand-name">BLUE<br>PINE</div>
      <div class="practice-type">FAMILY DENTISTRY</div>
    </div>
  </section>

  <section class="card card--front" aria-label="Card front">
    <div class="front-info">
      <div class="brand-name">BLUE<br>PINE</div>
      <div class="practice-type">FAMILY DENTISTRY</div>
      <div class="person-name">Daniel Morrow</div>
      <div class="person-title">Managing Director</div>
      <div class="address">4830 North Maple Loop Suite 208<br>Austin,Texas 78392</div>
      <ul class="contact-list">
        <li>
          <svg viewBox="0 0 24 24" aria-hidden="true"><path d="M6.6 10.8a15.1 15.1 0 0 0 6.6 6.6l2.2-2.2c.3-.3.7-.4 1-.2 1.1.4 2.3.6 3.6.6.6 0 1 .4 1 1V20c0 .6-.4 1-1 1A17 17 0 0 1 3 4c0-.6.4-1 1-1h3.5c.6 0 1 .4 1 1 0 1.3.2 2.5.6 3.6.1.3 0 .7-.2 1z"/></svg>
          512-847-3195
        </li>
        <li>
          <svg viewBox="0 0 24 24" aria-hidden="true"><path d="M2 5h20v14H2z M4 7v.5l8 5 8-5V7z" fill-rule="evenodd"/></svg>
          info@bluepinedental.example
        </li>
        <li>
          <svg viewBox="0 0 24 24" aria-hidden="true"><circle cx="12" cy="12" r="10"/></svg>
          www.BluePineDental.example
        </li>
      </ul>
    </div>

    <div class="front-mark">
      <div class="brand-dot"></div>
      <div class="brand-name">BLUE PINE</div>
    </div>
  </section>

</body>
</html>
```